Business Card Design for Varnok Facility Services

We are looking for a Business Card Design for the Company "Varnok Facility Services."
Front side:
- Company Logo (small)
- Company Name, address, pohone, website and personal data.
- white background, for text e.g. company colors (blue or green like in the logo)
Please use following data:
Company data:
Varnok Facility Services Tulbrecht
Kirchmattweg 12
6331 Cham
www.varnok-fs.ch
Person data:
Ruben Tulbrecht
Geschäftsführer
+41 76 519 84 60
info@varnok-fs.ch
Back side:
could be colored in blue or green
please use a big logo sing and some smaller icons to say what is all beeing offered in facility services, like cleaning, maintenance cleaning
industrial cleaning, caretaking, gardening, disposal. There is no need for everyone of the icons if there are similar or an icon is standing for more of them.
Cleaning Service
colors to use:
blue: HEX 246BB0
green: HEX 52B33E

```html
<!DOCTYPE html>
<html lang="de">
<head>
<meta charset="utf-8">
<title>Varnok Facility Services – Visitenkarte</title>
<link href="https://fonts.googleapis.com/css2?family=Source+Sans+3:ital,wght@0,400;0,600;0,700;1,600&display=swap" rel="stylesheet">
<style>
  :root {
    --blue: #246BB0;
    --green: #52B33E;
    --paper: #ffffff;
    --backdrop: #ffffff;
    --back-top: #4aa66a;
    --back-bottom: #2a8594;
    --shadow: rgba(0, 0, 0, 0.35);
  }
  * { margin: 0; padding: 0; box-sizing: border-box; }
  html, body {
    width: 1200px; height: 1200px; overflow: hidden;
    background: var(--backdrop);
    font-family: "Source Sans 3", "Myriad Pro", sans-serif;
  }
  .sheet { position: relative; width: 1200px; height: 1200px; }
  .card {
    position: absolute; left: 166px; width: 903px; height: 516px;
    box-shadow: 4px 5px 8px var(--shadow);
  }
  .card--front { top: 57px; background: var(--paper); }
  .card--back {
    top: 632px;
    background: linear-gradient(to bottom, var(--back-top), var(--back-bottom));
  }

  /* front: brand block */
  .brand {
    position: absolute; left: 46px; top: 200px; width: 340px;
    display: flex; align-items: center; justify-content: center; gap: 12px;
  }
  .brand__dot { width: 22px; height: 22px; border-radius: 50%; background: var(--green); flex: none; }
  .brand__name {
    color: var(--blue); font-weight: 700; font-size: 30px; line-height: 1.1;
  }
  .divider {
    position: absolute; left: 419px; top: 77px; width: 7px; height: 354px;
    background: var(--blue);
  }

  /* front: person */
  .person { position: absolute; right: 64px; top: 44px; text-align: right; }
  .person__name { color: var(--blue); font-size: 48px; font-weight: 400; line-height: 1; }
  .person__name b { font-weight: 700; }
  .person__role { color: var(--green); font-size: 26px; font-weight: 700; line-height: 1.2; }

  /* front: contact list */
  .contact { position: absolute; left: 0; top: 0; width: 100%; height: 100%; }
  .contact__row { position: absolute; left: 513px; color: var(--blue); font-weight: 600; font-size: 34px; line-height: 36px; }
  .contact__icon { position: absolute; left: -52px; }
  .contact__row--address { top: 192px; }
  .contact__row--address .contact__icon { top: 14px; }
  .contact__row--phone { top: 272px; }
  .contact__row--phone .contact__icon { top: -2px; }
  .contact__row--web { top: 322px; }
  .contact__row--web .contact__icon { top: 14px; }

  .tagline {
    position: absolute; left: 0; right: 0; top: 446px; text-align: center;
    color: var(--green); font-style: italic; font-weight: 600; font-size: 34px;
    letter-spacing: 2.5px;
  }

  /* back */
  .back-brand {
    position: absolute; left: 0; right: 0; top: 0; bottom: 0;
    display: flex; align-items: center; justify-content: center; gap: 26px;
  }
  .back-brand__dot { width: 60px; height: 60px; border-radius: 50%; background: var(--green); flex: none; }
  .back-brand__name {
    color: var(--blue); font-weight: 700; font-size: 68px; line-height: 1.05;
  }
</style>
</head>
<body>
<main class="sheet">
  <section class="card card--front" aria-label="Vorderseite">
    <div class="brand">
      <span class="brand__dot"></span>
      <span class="brand__name">Varnok<br>Facility Services</span>
    </div>
    <div class="divider"></div>

    <div class="person">
      <p class="person__name"><b>Ruben</b> Tulbrecht</p>
      <p class="person__role">Geschäftsführer</p>
    </div>

    <div class="contact">
      <p class="contact__row contact__row--address">
        <svg class="contact__icon" width="30" height="46" viewBox="0 0 30 46" aria-hidden="true">
          <path d="M15 1C7 1 1 7 1 15c0 10 14 30 14 30s14-20 14-30C29 7 23 1 15 1z" fill="var(--green)"/>
          <circle cx="15" cy="15" r="6" fill="#fff"/>
        </svg>
        Kirchmattweg 12,<br>6331 Cham
      </p>
      <p class="contact__row contact__row--phone">
        <svg class="contact__icon" width="40" height="40" viewBox="0 0 40 40" aria-hidden="true">
          <path d="M8 3l6 8-3 4c2 5 6 9 11 12l4-3 8 6-4 7C16 37 3 24 2 8z" fill="var(--green)"/>
          <path d="M24 5a11 11 0 0 1 11 11M24 10a6 6 0 0 1 6 6" stroke="var(--green)" stroke-width="2.5" fill="none" stroke-linecap="round"/>
        </svg>
        +41 76 519 84 60
      </p>
      <p class="contact__row contact__row--web">
        <svg class="contact__icon" width="40" height="40" viewBox="0 0 40 40" aria-hidden="true">
          <circle cx="20" cy="20" r="18" fill="var(--green)"/>
          <ellipse cx="20" cy="20" rx="8" ry="18" fill="none" stroke="#fff" stroke-width="2"/>
          <path d="M2 20h36M5 11h30M5 29h30" stroke="#fff" stroke-width="2"/>
        </svg>
        www.varnok-fs.ch<br>info@varnok-fs.ch
      </p>
    </div>

    <p class="tagline">Varnok Facility Services Tulbrecht</p>
  </section>

  <section class="card card--back" aria-label="Rückseite">
    <div class="back-brand">
      <span class="back-brand__dot"></span>
      <span class="back-brand__name">Varnok<br>Facility Services</span>
    </div>
  </section>
</main>
</body>
</html>
```